Zielgruppe
Die Kessler-Volkshochschule Kreis Aurental ist eine gemeinnützige Einrichtung zur Erwachsenen- und Weiterbildung mit ca. 5.000 Veranstaltungen pro Jahr.
Volkshochschulen sind entgegen ihrer Bezeichnung keine Hochschulen oder Schulen, sondern in Deutschland dem Bildungsbereich der Weiterbildung zugeordnet.
Aufgabenstellung
Die Kessler-Volkshochschule Kreis Aurental möchte mit einer neuen Webseite, welche auch für mobile Geräte geeignet sein muss, Ihren neuen Internetauftritt umsetzen.
Vorgaben:
- der Internetauftritt soll modern gestaltet sein.
- die unter Dateien befindlichen Guidelines müssen eingehalten werden. Wichtig hierbei ist, dass die 6 Symbole auf die Startseite für die Auswahl der jeweiligen Kursbereiche integriert werden. Hierbei ist zu beachten, dass die Anzahl der Symbole erweiterbar ist.
Als CMS wird Typo3 genutzt.
Es geht um die Erstellung der Startseite auf welcher auch News untergebracht werden sollen - ggf. in Kachelform. Und die Erstellung einer Unterseite.

```html
<!DOCTYPE html>
<html lang="de">
<head>
<meta charset="utf-8">
<title>Kessler-Volkshochschule – Startseite</title>
<link href="https://fonts.googleapis.com/css2?family=Open+Sans:wght@400;600;700&family=Signika:wght@600;700&display=swap" rel="stylesheet">
<style>
:root{
  --page:#f1f1f1;
  --white:#ffffff;
  --topbar:#d9dadc;
  --text:#4a4a4a;
  --muted:#8a8a8a;
  --nav-active:#6f7f8f;
  --orange:#ee7d1a;
  --green:#97c11f;
  --blue:#3b95d3;
  --purple:#7c3d96;
  --lime:#8cbd2a;
  --red:#e2231a;
  --amber:#f0a500;
  --tile:#f7f7f7;
}
*{box-sizing:border-box;margin:0;padding:0}
html,body{width:1200px;height:820px;overflow:hidden}
body{background:var(--page);font-family:"Open Sans",sans-serif;color:var(--text)}
.topbar{height:34px;background:var(--topbar);display:flex;align-items:center;gap:34px;padding-left:150px;font-size:12px;color:#555}
.topbar span{display:flex;align-items:center;gap:7px}
.header{height:76px;background:var(--white);display:flex;align-items:center;padding:0 100px;border-bottom:1px solid #e2e2e2}
.brand{display:flex;align-items:center;gap:10px;width:300px}
.brand-dot{width:14px;height:14px;border-radius:50%;background:var(--blue)}
.brand-name{font-size:14px;font-weight:600;color:#2f4a6b;line-height:1.2}
.nav{display:flex;gap:36px;align-items:center;font-size:11px;text-transform:uppercase;color:var(--muted);letter-spacing:.3px}
.nav .active{background:var(--nav-active);color:#fff;padding:6px 9px;border-radius:2px}
.nav .drop::before{content:"⌄ ";}
.cart{margin-left:auto;display:flex;align-items:center;gap:14px;font-size:11px;color:var(--muted)}
.slider{position:relative;margin:12px 100px 0;height:370px}
.slide-photo{position:absolute;inset:0;background:linear-gradient(180deg,#dfe7ec 0%,#8fa86a 30%,#7a6b55 60%,#3c3b38 100%)}
.arrow{position:absolute;top:140px;width:34px;height:40px;background:var(--orange);color:#fff;font-size:22px;display:flex;align-items:center;justify-content:center}
.arrow.prev{left:0}.arrow.next{right:0}
.headline{position:absolute;left:0;top:240px;font-family:"Signika",sans-serif;font-weight:700;color:#fff;font-size:40px;line-height:1}
.headline span{display:inline-block;padding:6px 14px}
.headline .l1{background:var(--orange)}
.headline .l2{background:var(--green)}
.dots{position:absolute;bottom:16px;left:50%;display:flex;gap:8px;transform:translateX(-50%)}
.dots i{width:8px;height:8px;border-radius:50%;background:#ddd;display:block}
.dots i.on{background:#2f4a6b}
.portal{position:absolute;right:34px;top:0;width:120px;background:#fff;padding:8px;font-size:7px;color:#666;box-shadow:0 2px 6px rgba(0,0,0,.2);border-top:3px solid var(--orange)}
.portal h4{font-size:7px;font-weight:600;margin-bottom:6px}
.portal .field{height:10px;border:1px solid #ccc;margin:3px 0 6px}
.portal .btns{display:flex;gap:4px}
.portal .btns span{background:var(--orange);color:#fff;padding:2px 5px}
.portal a{display:block;color:var(--blue);margin-top:4px}
.areas{display:flex;gap:14px;margin:18px 100px 0}
.area{flex:1;height:186px;background:var(--tile);box-shadow:0 1px 3px rgba(0,0,0,.12);text-align:center;padding-top:26px}
.icon{width:70px;height:70px;border-radius:50%;margin:0 auto 12px;display:flex;align-items:center;justify-content:center}
.area h3{font-size:10px;font-weight:700;letter-spacing:.4px;margin-bottom:6px}
.area p{font-size:8.5px;line-height:1.5;color:#666;padding:0 14px}
.pager{display:flex;justify-content:flex-end;gap:4px;margin:10px 100px 0}
.pager span{width:18px;height:18px;background:#b8bec6;color:#fff;font-size:11px;display:flex;align-items:center;justify-content:center}
.pager span.on{background:#2f4a6b}
.news-title{margin:18px 100px 0;font-size:20px;font-weight:600;color:#555}
</style>
</head>
<body>
<div class="topbar">
  <span><svg width="12" height="12" viewBox="0 0 24 24"><path fill="#555" d="M6.6 10.8a15 15 0 0 0 6.6 6.6l2.2-2.2c.3-.3.7-.4 1-.2 1.1.4 2.3.6 3.6.6.6 0 1 .4 1 1V20c0 .6-.4 1-1 1A17 17 0 0 1 3 4c0-.6.4-1 1-1h3.5c.6 0 1 .4 1 1 0 1.3.2 2.5.6 3.6.1.3 0 .7-.2 1z"/></svg>04821 557-2030</span>
  <span><svg width="13" height="10" viewBox="0 0 26 20"><rect x="1" y="1" width="24" height="18" fill="none" stroke="#555" stroke-width="2"/><path d="M1 1l12 10L25 1" fill="none" stroke="#555" stroke-width="2"/></svg>info@kessler-vhs.de</span>
</div>
<header class="header">
  <div class="brand"><span class="brand-dot"></span><div class="brand-name">Kessler-Volkshochschule<br>Kreis Aurental</div></div>
  <nav class="nav">
    <span class="active">Startseite</span><span>Kursprogramm</span><span class="drop">Förderungen</span><span>Service</span><span>Kontakt</span>
  </nav>
  <div class="cart">
    <svg width="10" height="12" viewBox="0 0 10 12"><rect x="1" y="5" width="8" height="7" fill="var(--orange)"/><path d="M2.5 5V3.5a2.5 2.5 0 0 1 5 0V5" fill="none" stroke="var(--orange)" stroke-width="1.4"/></svg>
    <span>🛒︎ 0 Kurse</span>
  </div>
</header>
<section class="slider">
  <div class="slide-photo" role="img" aria-label="Foto: Gruppe von Teilnehmern bei einer Ortsbegehung neben einem Sportplatz"></div>
  <div class="arrow prev">«</div><div class="arrow next">»</div>
  <div class="headline"><span class="l1">„Politik Live“ in</span><br><span class="l2">Haselbrunn</span></div>
  <div class="dots"><i></i><i></i><i class="on"></i><i></i></div>
  <div class="portal">
    <h4>TEILNEHMER PORTAL</h4>
    Ihre Teilnehmer-Nr.<div class="field"></div>
    Ihr Passwort<div class="field"></div>
    <div class="btns"><span>Anmelden</span><span>Login</span></div>
    <a>Teilnehmer-Nr. vergessen?</a><a>Passwort vergessen?</a>
  </div>
</section>
<section class="areas">
  <div class="area"><div class="icon" style="background:var(--blue)"><svg width="34" height="28"><rect x="4" y="8" width="26" height="18" rx="2" fill="#fff"/><rect x="12" y="3" width="10" height="6" fill="none" stroke="#fff" stroke-width="2"/></svg></div><h3>BERUF</h3><p>Er hörte leise Schritte hinter sich. Das bedeutete nichts Gutes.</p></div>
  <div class="area"><div class="icon" style="background:var(--purple)"><svg width="34" height="28"><path d="M3 3h28v16H14l-7 6v-6H3z" fill="#fff"/></svg></div><h3>SPRACHEN</h3><p>Er hörte leise Schritte hinter sich. Das bedeutete nichts Gutes.</p></div>
  <div class="area"><div class="icon" style="background:var(--lime)"><svg width="34" height="28"><path d="M17 25S4 17 4 9a6 6 0 0 1 13-2 6 6 0 0 1 13 2c0 8-13 16-13 16z" fill="#fff"/></svg></div><h3>GESUNDHEIT</h3><p>Er hörte leise Schritte hinter sich. Das bedeutete nichts Gutes.</p></div>
  <div class="area"><div class="icon" style="background:var(--red)"><svg width="34" height="28"><path d="M12 4v16M26 2v16M12 4l14-2" stroke="#fff" stroke-width="2.5" fill="none"/><circle cx="9" cy="21" r="4" fill="#fff"/><circle cx="23" cy="19" r="4" fill="#fff"/></svg></div><h3>KULTUR</h3><p>Er hörte leise Schritte hinter sich. Das bedeutete nichts Gutes.</p></div>
  <div class="area"><div class="icon" style="background:var(--orange)"><svg width="34" height="28"><rect x="5" y="3" width="24" height="16" fill="none" stroke="#fff" stroke-width="2.5"/><path d="M12 25l5-6 5 6" stroke="#fff" stroke-width="2.5" fill="none"/></svg></div><h3>KULTUR</h3><p>Er hörte leise Schritte hinter sich. Das bedeutete nichts Gutes.</p></div>
  <div class="area"><div class="icon" style="background:var(--amber)"><svg width="34" height="28"><path d="M3 5h12l2 2 2-2h12v19H19l-2 2-2-2H3z" fill="#fff"/></svg></div><h3>GRUNDBILDUNG</h3><p>Er hörte leise Schritte hinter sich. Das bedeutete nichts Gutes.</p></div>
</section>
<div class="pager"><span>‹</span><span class="on">›</span></div>
<h2 class="news-title">Unsere neuesten Beiträge</h2>
</body>
</html>
```